Need a business card design. I am a Self Empowerment Life Coach.

A Life Coach is - a professional relationship designed to enhance an individual's ability to focus, make effective changes, develop oneself, achieve desired goals and maximize success in life. Coaching is about getting the very best out of someone and enabling them to make decisions that will improve their life. It is a unique way to help people look at where they are now and where they would like to be, and helps bridge the gap.

Bright Path Coaching is motivational, inspiring, positive, exciting and action driven. By raising awareness and encouraging others to take responsibility for their life, coaching can help people rise to their challenge and go further than you ever thought possible.

Industry/Entity Type

Business

Other font styles liked:
• Bookman Old Style

Requirements
Must have
• Marla Thorncastle, QTV-AR
• Self Empowerment Coach
• 318.557.6021
• mt@thebloomingpathcoach.example
• The attached logo
Nice to have
• I would like to see some designs portrait and some landscape

```html
<!DOCTYPE html>
<html lang="en">
<head>
<meta charset="utf-8">
<title>Blooming Path Coaching – Business Card Options</title>
<link href="https://fonts.googleapis.com/css2?family=Oswald:wght@700&family=Didact+Gothic&family=Tinos:wght@700&family=Arimo:wght@700&display=swap" rel="stylesheet">
<style>
  :root{
    --sheet:#ffffff;
    --card-edge:#d9dde0;
    --brand-blue:#1d5a92;
    --name-teal:#1f5a6c;
    --name-light:#8fc8de;
    --title-teal:#3d6f7e;
    --tag-blue:#2c6f9c;
    --contact-ink:#1f4f5f;
    --rule-dark:#6b6f72;
    --icon-grey:#b9bdbf;
    --wash:#cfe8f1;
  }
  *{box-sizing:border-box;margin:0;padding:0}
  html,body{width:900px;height:1200px;overflow:hidden;background:var(--sheet)}
  .sheet{position:relative;width:900px;height:1200px}
  .card{position:absolute;background:#fff;border:1px solid var(--card-edge);overflow:hidden}
  .card--wash{background:linear-gradient(180deg,#fff 0%,#eef7fa 22%,var(--wash) 50%,#eef7fa 78%,#fff 100%)}
  .card--landscape-a{left:6px;top:137px;width:460px;height:307px}
  .card--landscape-b{left:488px;top:137px;width:407px;height:307px}
  .card--portrait-a{left:15px;top:534px;width:356px;height:611px}
  .card--portrait-b{left:395px;top:493px;width:502px;height:680px}
  .el{position:absolute;white-space:nowrap}
  .brand-name{font-family:'Oswald',sans-serif;font-weight:700;color:var(--brand-blue);text-align:center;text-transform:uppercase;line-height:1.02;letter-spacing:.5px}
  .tagline{font-family:'Didact Gothic',sans-serif;color:var(--tag-blue);text-transform:uppercase;text-align:center;letter-spacing:1.5px}
  .tada{font-family:'Didact Gothic',sans-serif;color:var(--tag-blue);text-align:center;letter-spacing:5px}
  .coach-name{font-family:'Oswald',sans-serif;font-weight:700;color:var(--name-teal);text-transform:uppercase;text-align:center}
  .coach-name--light{color:var(--name-light)}
  .coach-title{font-family:'Didact Gothic',sans-serif;color:var(--title-teal);text-transform:uppercase;text-align:center;letter-spacing:1.2px}
  .phone{font-family:'Tinos',serif;font-weight:700;color:var(--contact-ink);display:flex;align-items:center;gap:10px}
  .email{font-family:'Arimo',sans-serif;font-weight:700;color:var(--contact-ink);display:flex;align-items:center;gap:7px}
  .icon{flex:none;border:1.5px solid var(--icon-grey);border-radius:50%;display:flex;align-items:center;justify-content:center;color:var(--icon-grey);font-family:'Arimo',sans-serif}
  .rule{position:absolute;height:4px;border-radius:50%;background:radial-gradient(ellipse at center,var(--rule-dark) 0%,rgba(107,111,114,.7) 55%,rgba(107,111,114,0) 100%)}
</style>
</head>
<body>
<main class="sheet">

  <section class="card card--landscape-a">
    <div class="el brand-name" style="left:22px;top:102px;width:160px;font-size:34px">Blooming<br>Path<br>Coaching</div>
    <div class="rule" style="left:6px;top:247px;width:215px"></div>
    <div class="el tagline" style="left:6px;top:256px;width:215px;font-size:11px">Step from stuck to</div>
    <div class="el tada" style="left:6px;top:268px;width:215px;font-size:30px">ONWARD!</div>
    <div class="rule" style="left:200px;top:100px;width:205px"></div>
    <div class="el coach-name" style="left:196px;top:106px;width:220px;font-size:17px">Marla Thorncastle, QTV-AR</div>
    <div class="el coach-title" style="left:196px;top:131px;width:220px;font-size:13px">Self Empowerment Coach</div>
    <div class="el phone" style="left:234px;top:156px;font-size:18px">
      <span class="icon" style="width:18px;height:18px"><svg width="10" height="10" viewBox="0 0 24 24"><path fill="#b9bdbf" d="M6.6 10.8a15 15 0 0 0 6.6 6.6l2.2-2.2a1 1 0 0 1 1-.25 11.4 11.4 0 0 0 3.6.57 1 1 0 0 1 1 1V20a1 1 0 0 1-1 1A17 17 0 0 1 3 4a1 1 0 0 1 1-1h3.5a1 1 0 0 1 1 1c0 1.25.2 2.45.57 3.6a1 1 0 0 1-.25 1z"/></svg></span>318.557.6021</div>
    <div class="el email" style="left:200px;top:186px;font-size:10.5px">
      <span class="icon" style="width:17px;height:17px;font-size:10px">@</span>mt@thebloomingpathcoach.example</div>
    <div class="rule" style="left:200px;top:211px;width:205px"></div>
  </section>

  <section class="card card--landscape-b card--wash">
    <div class="el brand-name" style="left:16px;top:106px;width:146px;font-size:30px">Blooming<br>Path<br>Coaching</div>
    <div class="rule" style="left:4px;top:247px;width:200px"></div>
    <div class="el tagline" style="left:4px;top:256px;width:200px;font-size:11px">Step from stuck to</div>
    <div class="el tada" style="left:4px;top:268px;width:200px;font-size:30px">ONWARD!</div>
    <div class="rule" style="left:170px;top:100px;width:226px"></div>
    <div class="el coach-name" style="left:166px;top:106px;width:234px;font-size:16px">Marla Thorncastle, QTV-AR</div>
    <div class="el coach-title" style="left:166px;top:130px;width:234px;font-size:12.5px">Self Empowerment Coach</div>
    <div class="el phone" style="left:212px;top:155px;font-size:18px">
      <span class="icon" style="width:18px;height:18px"><svg width="10" height="10" viewBox="0 0 24 24"><path fill="#b9bdbf" d="M6.6 10.8a15 15 0 0 0 6.6 6.6l2.2-2.2a1 1 0 0 1 1-.25 11.4 11.4 0 0 0 3.6.57 1 1 0 0 1 1 1V20a1 1 0 0 1-1 1A17 17 0 0 1 3 4a1 1 0 0 1 1-1h3.5a1 1 0 0 1 1 1c0 1.25.2 2.45.57 3.6a1 1 0 0 1-.25 1z"/></svg></span>318.557.6021</div>
    <div class="el email" style="left:174px;top:186px;font-size:10px">
      <span class="icon" style="width:17px;height:17px;font-size:10px">@</span>mt@thebloomingpathcoach.example</div>
    <div class="rule" style="left:170px;top:211px;width:226px"></div>
  </section>

  <section class="card card--portrait-a">
    <div class="el brand-name" style="left:78px;top:118px;width:200px;font-size:44px">Blooming<br>Path<br>Coaching</div>
    <div class="rule" style="left:56px;top:300px;width:244px"></div>
    <div class="el tagline" style="left:0;top:312px;width:356px;font-size:12px">Step from stuck to</div>
    <div class="el tada" style="left:0;top:322px;width:356px;font-size:34px">ONWARD!</div>
    <div class="rule" style="left:10px;top:366px;width:336px;height:5px"></div>
    <div class="el coach-name coach-name--light" style="left:0;top:388px;width:356px;font-size:22px">Marla Thorncastle, QTV-AR</div>
    <div class="el coach-title" style="left:0;top:428px;width:356px;font-size:16px">Self Empowerment Coach</div>
    <div class="rule" style="left:10px;top:462px;width:336px;height:5px"></div>
    <div class="el phone" style="left:28px;top:482px;font-size:29px">
      <span class="icon" style="width:34px;height:34px"><svg width="18" height="18" viewBox="0 0 24 24"><path fill="#b9bdbf" d="M6.6 10.8a15 15 0 0 0 6.6 6.6l2.2-2.2a1 1 0 0 1 1-.25 11.4 11.4 0 0 0 3.6.57 1 1 0 0 1 1 1V20a1 1 0 0 1-1 1A17 17 0 0 1 3 4a1 1 0 0 1 1-1h3.5a1 1 0 0 1 1 1c0 1.25.2 2.45.57 3.6a1 1 0 0 1-.25 1z"/></svg></span>318.557.6021</div>
    <div class="el email" style="left:8px;top:536px;font-size:14px">
      <span class="icon" style="width:30px;height:30px;font-size:16px">@</span>mt@thebloomingpathcoach.example</div>
  </section>

  <section class="card card--portrait-b card--wash">
    <div class="el brand-name" style="left:136px;top:140px;width:230px;font-size:52px">Blooming<br>Path<br>Coaching</div>
    <div class="rule" style="left:100px;top:356px;width:302px"></div>
    <div class="el tagline" style="left:0;top:368px;width:502px;font-size:15px">Step from stuck to</div>
    <div class="el tada" style="left:0;top:380px;width:502px;font-size:40px">ONWARD!</div>
    <div class="rule" style="left:80px;top:436px;width:342px;height:5px"></div>
    <div class="el coach-name" style="left:0;top:450px;width:502px;font-size:24px">Marla Thorncastle, QTV-AR</div>
    <div class="el coach-title" style="left:0;top:494px;width:502px;font-size:19px">Self Empowerment Coach</div>
    <div class="rule" style="left:80px;top:528px;width:342px;height:5px"></div>
    <div class="el phone" style="left:140px;top:538px;font-size:25px">
      <span class="icon" style="width:32px;height:32px"><svg width="17" height="17" viewBox="0 0 24 24"><path fill="#b9bdbf" d="M6.6 10.8a15 15 0 0 0 6.6 6.6l2.2-2.2a1 1 0 0 1 1-.25 11.4 11.4 0 0 0 3.6.57 1 1 0 0 1 1 1V20a1 1 0 0 1-1 1A17 17 0 0 1 3 4a1 1 0 0 1 1-1h3.5a1 1 0 0 1 1 1c0 1.25.2 2.45.57 3.6a1 1 0 0 1-.25 1z"/></svg></span>318.557.6021</div>
    <div class="el email" style="left:64px;top:580px;font-size:17px">
      <span class="icon" style="width:32px;height:32px;font-size:17px">@</span>mt@thebloomingpathcoach.example</div>
  </section>

</main>
</body>
</html>
```